JesterVolt Balloon Logo and Product Packaging Design

I need a package design for twisting balloons for my website jestervoltfun.com. The brand name that we will use is "jestervolt". The packaging will be 40cm long x 15 cm width with a see thru front and a top that can tear off. We can only use 3 colors max, but two colors would be better. We also will need a logo for "jestervolt". I have included our mockup front and back, our competitors packaging and our style guide. You can use our style guide and our mockups for inspiration but you please don't follow it exactly. You can also ignore them all together. Thanks, Corin

```html
<!DOCTYPE html>
<html lang="en">
<head>
<meta charset="utf-8">
<title>JesterVolt Twisting Balloons – Packaging</title>
<link rel="stylesheet" href="https://fonts.googleapis.com/css2?family=Luckiest+Guy&family=Pathway+Gothic+One&family=Poppins:wght@400;600;700;800&display=swap">
<style>
  :root {
    --brand-red: #bf1f2f;
    --brand-blue: #3a86f0;
    --ink: #1b1b1b;
    --paper: #ffffff;
    --frame: #111111;
  }
  * { box-sizing: border-box; margin: 0; padding: 0; }
  html, body { width: 1076px; height: 1200px; overflow: hidden; background: var(--paper); }
  .canvas { position: relative; width: 1076px; height: 1200px; }

  .panel {
    position: absolute; top: 111px; width: 372px; height: 983px;
    border: 6px solid var(--frame); background: var(--paper); overflow: hidden;
  }
  .panel--back { left: 140px; }
  .panel--front { left: 571px; }
  .panel__waves { position: absolute; left: -6px; top: -6px; width: 372px; height: 983px; }

  .brand-tag {
    position: absolute; left: 52px; top: 70px;
    font-family: "Luckiest Guy", cursive; font-size: 12.5px; color: var(--paper);
    letter-spacing: 0.5px; transform: rotate(6deg); transform-origin: left center;
  }
  .brand-name {
    position: absolute; font-family: "Poppins", sans-serif; font-weight: 800;
    color: var(--brand-blue); font-size: 40px; letter-spacing: -0.5px; line-height: 1;
  }
  .panel--back .brand-name { left: 40px; top: 105px; }
  .panel--front .brand-name { left: 38px; top: 128px; }

  .copy {
    position: absolute; left: 20px; top: 202px; width: 320px;
    font-family: "Pathway Gothic One", sans-serif; font-size: 16.2px; line-height: 18.45px;
    color: var(--ink); text-align: center; hyphens: auto;
  }

  .symbols { position: absolute; left: 16px; top: 688px; display: flex; gap: 17px; align-items: center; }
  .symbols svg { width: 32px; height: 34px; }

  .facts {
    position: absolute; top: 746px; font-family: "Pathway Gothic One", sans-serif;
    font-size: 16.5px; color: #333;
  }
  .facts--origin { left: 16px; }
  .facts--weight { left: 115px; }

  .latex-note {
    position: absolute; left: 202px; top: 690px; width: 148px; height: 110px;
    border: 1.2px solid #333; border-radius: 9px;
    font-family: "Pathway Gothic One", sans-serif; font-size: 18.5px; line-height: 22px;
    color: var(--ink); text-align: center; padding-top: 9px;
  }
  .latex-note strong { font-weight: 400; font-size: 20px; letter-spacing: 0.3px; -webkit-text-stroke: 0.5px var(--ink); }

  .company {
    position: absolute; right: 26px; top: 900px; text-align: right;
    font-family: "Poppins", sans-serif; color: var(--paper); letter-spacing: 1.3px;
    font-size: 14.5px; line-height: 19.5px;
  }
  .company__name { font-weight: 700; }
  .company__web { font-weight: 600; }
  .company__city { font-weight: 400; }

  .side-line {
    position: absolute; left: 22px; top: 238px;
    writing-mode: vertical-rl; font-family: "Luckiest Guy", cursive;
    font-size: 23px; letter-spacing: 0.6px; line-height: 1;
  }
  .side-line__claim { color: var(--brand-blue); }
  .side-line__count { color: var(--brand-red); margin-top: 38px; display: inline-block; }

  .warning { position: absolute; left: 0; top: 756px; width: 360px; color: var(--paper); font-family: "Poppins", sans-serif; }
  .warning__icon { position: absolute; left: 52px; top: 0; width: 60px; height: 52px; }
  .warning__title { position: absolute; left: 52px; top: 72px; font-weight: 700; font-size: 15.5px; letter-spacing: 1.3px; }
  .warning__text {
    position: absolute; left: 18px; top: 101px; width: 330px; text-align: center;
    font-weight: 600; font-size: 11.6px; line-height: 17.6px; letter-spacing: 0.3px;
  }
</style>
</head>
<body>
<main class="canvas">

  <section class="panel panel--back" aria-label="Back of pack">
    <svg class="panel__waves" viewBox="0 0 372 983" aria-hidden="true">
      <path fill="var(--brand-red)" d="M0 62 C60 48 120 46 180 60 C250 76 300 92 372 78 L372 182 C330 190 300 192 260 184 C200 170 140 150 90 152 C50 154 20 160 0 164 Z"/>
      <path fill="var(--brand-red)" d="M0 910 C60 910 100 904 160 880 C230 850 290 838 372 890 L372 983 L0 983 Z"/>
    </svg>

    <p class="brand-tag">High-Quality Party Balloons</p>
    <p class="brand-name">JesterVolt</p>

    <div class="copy">
      <p>Lorem ipsum dolor sit amet, consectetuer adipiscing elit, sed diam nonummy nibh euismod tincidunt ut laoreet dolore magna aliquam erat volutpat. Ut wisi enim ad minim veniam, quis nostrud exerci tation ullamcorper suscipit lobortis nisl ut aliquip ex ea commodo consequat. Duis autem vel eum iriure dolor in hendrerit in vulputate velit esse molestie consequat, vel illum dolore eu feugiat nulla facilisis at vero eros et accumsan et iusto odio dignissim qui blandit praesent luptatum zzril delenit augue duis dolore te feugait nulla facilisi.</p>
      <p>Lorem ipsum dolor sit amet, cons ectetuer adipiscing elit, sed diam nonummy nibh euismod tincidunt ut laoreet dolore magna aliquam erat volutpat. Ut wisi enim ad minim veniam, quis nostrud exerci tation ullamcorper suscipit lobortis nisl ut aliquip ex ea commodo consequat.</p>
      <p>Lorem ipsum dolor sit amet, consectetuer adipiscing elit, sed diam nonummy nibh euismod tincidunt ut laoreet dolore magna aliquam erat volutpat. Ut wisi enim ad minim veniam, quis nostrud exerci tation ullamcorper suscipit lobortis nisl ut aliquip ex ea commodo consequat. Duis autem vel eum iriure dolor in hendrerit in vulputate velit esse molestie consequat, vel illum dolore eu feugiat nulla facilisis at vero eros et accumsan et iusto odio dignissim qui blandit praesent luptatum zzril delenit augue duis dolore te feugait nulla fac-</p>
    </div>

    <div class="symbols">
      <svg viewBox="0 0 32 34" role="img" aria-label="Dispose in bin symbol">
        <path fill="#222" d="M4 16 h11 l-1.5 15 h-8 Z M3 13 h13 v2 H3 Z"/>
        <circle cx="24" cy="5" r="3" fill="#222"/>
        <path fill="#222" d="M21 9 h6 l1 12 -2 11 h-3 l1-10 -2 10 h-3 l1-12 -5-4 2-2 4 3 Z"/>
      </svg>
      <svg viewBox="0 0 34 34" role="img" aria-label="Not suitable for children under 3">
        <circle cx="17" cy="17" r="14.5" fill="none" stroke="#e2233a" stroke-width="3"/>
        <line x1="7" y1="7" x2="27" y2="27" stroke="#e2233a" stroke-width="3"/>
      </svg>
      <svg viewBox="0 0 32 34" role="img" aria-label="Recycling mark">
        <path fill="none" stroke="#222" stroke-width="3.5" stroke-linejoin="round" d="M16 5 L27 25 H5 Z"/>
      </svg>
      <svg viewBox="0 0 34 34" role="img" aria-label="Conformity mark">
        <rect x="4" y="7" width="26" height="20" fill="#222"/>
      </svg>
    </div>

    <p class="facts facts--origin">Made in China</p>
    <p class="facts facts--weight">Net Wt. 25g</p>

    <div class="latex-note">
      <strong>Made of 100%</strong><br>
      Natural Rubber Latex<br>
      which may cause<br>
      allergic reactions
    </div>

    <address class="company" style="font-style: normal;">
      <span class="company__name">JesterVolt</span><br>
      <span class="company__web">www.jestervoltfun.com</span><br>
      <span class="company__city">Millbrook Falls, New York</span>
    </address>
  </section>

  <section class="panel panel--front" aria-label="Front of pack">
    <svg class="panel__waves" viewBox="0 0 372 983" aria-hidden="true">
      <path fill="var(--brand-red)" d="M0 108 C40 102 80 96 130 98 C190 101 240 122 290 124 C320 124 350 120 372 118 L372 200 C340 206 310 204 280 198 C220 186 180 176 130 178 C80 180 40 186 0 188 Z"/>
      <path fill="var(--brand-red)" d="M0 758 C50 735 90 722 130 722 C190 722 240 760 290 774 C320 780 350 778 372 772 L372 983 L0 983 Z"/>
    </svg>

    <p class="brand-name">JesterVolt</p>

    <p class="side-line">
      <span class="side-line__claim">High-Quality Party Balloons</span>
      <span class="side-line__count">100 PCS</span>
    </p>

    <div class="warning">
      <svg class="warning__icon" viewBox="0 0 60 52" role="img" aria-label="Warning">
        <path d="M30 3 L57 49 H3 Z" fill="none" stroke="var(--paper)" stroke-width="3" stroke-linejoin="round"/>
        <rect x="28" y="17" width="4" height="18" rx="1.5" fill="var(--paper)"/>
        <circle cx="30" cy="41" r="2.4" fill="var(--paper)"/>
      </svg>
      <p class="warning__title">WARNING: CHOKING HAZARD</p>
      <p class="warning__text">Children under 8 years old can choke or suffocate on uninflated or broken balloons. adult supervision is required. keep uninflated balloons from reach of children. discard broken balloons responsibly.</p>
    </div>
  </section>

</main>
</body>
</html>
```